-Photo booth rental Web Design Project

Our business is a small photo booth rental service serving the capital region and surrounding areas. The photo booth is a portable booth that fits up to 10 guest. I am looking for a website that will have social media capabilities and also private log ins for clients to view their photo albums online after their event. We provide full service photo booth rentals for all types of parties. I am looking for something fun and unique but also professional and I am also looking to maybe somehow incorporate the age of the photo booth which was invented in 1888. I do not have the photos of our photo booth available because we are just starting up and I wanted to get everything together first but I will provide stock photo booth pictures .Thank you for your patience i know it wont be an easy task with out those things. I added a word document describing information i will need on our website, i am looking for a home page, contact us and book an event page, online gallery page, and pricing. If you need any more information please feel free to contact me. Thanks for your help and I look forward to working with you.

Target Market(s)

For everyone from brides to be for their weddings or private parties, corporate parties, school dances, charity events, community events ect

Industry/Entity Type

Business

Requirements
Nice to have
• social media sharing

```html
<!DOCTYPE html>
<html lang="en">
<head>
<meta charset="utf-8">
<title>Giggle Frame Photo Booth</title>
<link href="https://fonts.googleapis.com/css2?family=Parisienne&family=Roboto+Condensed:wght@500&display=swap" rel="stylesheet">
<style>
  :root {
    --sun: #e8d53b;
    --glow: #f7f0a4;
    --band: #d3c42f;
    --tag: #ff9f0f;
    --ink: #2b231d;
    --paper: #ffffff;
  }
  * { margin: 0; padding: 0; box-sizing: border-box; }
  html, body { width: 1200px; height: 1000px; overflow: hidden; }
  body {
    position: relative;
    background:
      radial-gradient(ellipse 360px 230px at 600px 370px, var(--glow) 0%, rgba(247,240,164,0.55) 40%, rgba(232,213,59,0) 100%),
      var(--sun);
    font-family: "Roboto Condensed", sans-serif;
  }
  .corner { position: absolute; }
  .corner--top { left: 0; top: 0; }
  .corner--bottom { right: 0; bottom: 0; }

  .nav-tag {
    position: absolute;
    width: 228px;
    height: 52px;
    margin: -26px 0 0 -114px;
    background: var(--tag);
    transform: rotate(-13deg);
    box-shadow: 4px 6px 6px rgba(0,0,0,0.3);
    color: var(--paper);
    font-family: "Parisienne", cursive;
    font-size: 31px;
    line-height: 52px;
    text-align: center;
    text-decoration: none;
  }
  .nav-tag--home { left: 232px; top: 130px; }
  .nav-tag--pricing { left: 607px; top: 129px; }
  .nav-tag--contact { left: 975px; top: 129px; }
  .nav-tag--book { left: 412px; top: 570px; }
  .nav-tag--login { left: 800px; top: 570px; }

  .brand {
    position: absolute;
    left: 360px;
    top: 300px;
    width: 480px;
    display: flex;
    align-items: center;
    gap: 18px;
    color: var(--ink);
  }
  .brand__dot {
    width: 64px; height: 64px;
    border-radius: 50%;
    background: var(--ink);
    flex: none;
  }
  .brand__name {
    font-size: 50px;
    line-height: 54px;
    font-weight: 500;
  }

  .intro {
    position: absolute;
    left: 0; top: 690px;
    width: 1200px; height: 245px;
    background: var(--band);
    box-shadow: 0 12px 14px rgba(120,110,10,0.35);
    padding-top: 20px;
  }
  .intro p {
    width: 850px;
    margin: 0 auto;
    color: var(--paper);
    font-size: 20px;
    line-height: 30px;
    text-align: center;
  }
</style>
</head>
<body>
  <svg class="corner corner--top" width="180" height="40" viewBox="0 0 180 40"><polygon points="0,0 180,0 0,40" fill="#ff9f0f"/></svg>
  <svg class="corner corner--bottom" width="190" height="42" viewBox="0 0 190 42"><polygon points="190,0 190,42 0,42" fill="#ff9f0f"/></svg>

  <nav>
    <a class="nav-tag nav-tag--home" href="#">Home</a>
    <a class="nav-tag nav-tag--pricing" href="#">Pricing</a>
    <a class="nav-tag nav-tag--contact" href="#">Contact Us</a>
    <a class="nav-tag nav-tag--book" href="#">Book An Event</a>
    <a class="nav-tag nav-tag--login" href="#">Client Log In</a>
  </nav>

  <div class="brand">
    <span class="brand__name">Giggle Frame<br>Photo Booth</span>
    <span class="brand__dot"></span>
  </div>

  <section class="intro">
    <p>Our Booths feature the latest equipment and technology with TapSense screens, FriendPage and email uploading, TunePlay ready speaker systems, and dual "Photo Booth" or "Video Booth" modes with 1080p HD.<br>
    Fun entertainment &amp; favors for all event types, ex: weddings, birthday parties, graduations, holiday parties, corporate parties, bar/ bat mitzvahs, bridal showers, baby showers, anniversaries, grand openings, school events, proms, corporate events, promotional events, trade shows, conventions, community &amp; charity events</p>
  </section>
</body>
</html>
```